Startup internet service provider needs door hanger and post card design

We are a startup internet service provider in Colorado, and we need some marketing materials. We provide internet service to home and business. This is a competitive market so we need something that will catch our potential customers eye. Brookvale Networks offers fast and reliable internet service without the headaches. No long term contracts or special promotions that expire and raise your rate. We offer a simple monthly rate with bills and features that are easy to understand.

Target Market(s)

Home and business internet subscribers

Colors
0555a3
acd036

Requirements
Must have
• Simple and professional
reference to website
https://brookvale-networks.example/
Nice to have
• qr code scan for website

```html
<!DOCTYPE html>
<html lang="en">
<head>
<meta charset="utf-8">
<title>Brookvale Networks – Postcard</title>
<link href="https://fonts.googleapis.com/css2?family=Poppins:wght@400;500;600;700;800&display=swap" rel="stylesheet">
<style>
:root{
  --brand-blue:#0555a3;
  --deep-blue:#0a3f8f;
  --navy:#0d2f6b;
  --brand-green:#acd036;
  --ink:#111111;
  --white:#ffffff;
  --stamp:#eff1f1;
  --backdrop:#b1b3b3;
}
*{margin:0;padding:0;box-sizing:border-box}
html,body{width:1200px;height:1200px;overflow:hidden}
body{background:var(--backdrop);position:relative;font-family:'Poppins',sans-serif}
.card{position:absolute;width:1124px;height:787px;background:var(--white);overflow:hidden;transform-origin:0 0;transform:scale(.621)}
.card--front{left:251px;top:62px}
.card--back{left:251px;top:637px}
.shapes{position:absolute;inset:0;width:1124px;height:787px}
.abs{position:absolute}
.brand{display:flex;align-items:center;gap:12px;color:var(--navy);font-weight:500;white-space:nowrap}
.brand__dot{width:58px;height:58px;border-radius:50%;background:var(--brand-blue)}
.headline-bar{width:5px;background:var(--brand-green)}
.headline{color:var(--brand-green);font-weight:800;letter-spacing:.5px;text-transform:uppercase;white-space:nowrap}
.subtitle{color:var(--white);font-weight:500;white-space:nowrap}
.divider{height:4px;background:var(--white)}
.divider::before{content:"";position:absolute;left:0;top:-2px;width:64px;height:8px;background:var(--brand-green)}
.about{color:var(--white);font-size:24.5px;line-height:29.5px;white-space:nowrap}
.about strong{color:var(--brand-green);font-weight:700}
.photo{border-radius:50%;border:13px solid var(--brand-green);background:radial-gradient(circle at 50% 60%,#d9a98a 0%,#b7876c 30%,#8d8a82 60%,#c9c4b8 100%)}
.cta{display:flex;align-items:center;gap:12px;font-weight:800;text-transform:uppercase;white-space:nowrap}
.phone-line{display:flex;align-items:center;gap:14px;font-weight:700;color:var(--ink);white-space:nowrap}
.web-line{display:flex;align-items:center;gap:14px;color:var(--ink);white-space:nowrap}
.checklist{list-style:none}
.checklist li{display:flex;align-items:center;gap:14px;color:var(--white);font-size:23.5px;height:45px;white-space:nowrap}
.stamp-box{background:var(--stamp)}
.address-line{height:2px;background:#333}
</style>
</head>
<body>

<section class="card card--front">
  <svg class="shapes" viewBox="0 0 1124 787" aria-hidden="true">
    <defs>
      <linearGradient id="blueFill" x1="0" y1="0" x2="1" y2="1">
        <stop offset="0" stop-color="#0a4fa0"/>
        <stop offset="1" stop-color="#0a3d8c"/>
      </linearGradient>
    </defs>
    <path d="M1090,0 C1075,55 1055,100 1030,130 L1060,400 C1085,440 1105,470 1124,490 L1124,0 Z" fill="var(--brand-green)"/>
    <path d="M1105,0 C1090,60 1065,105 1040,135 L1070,400 C1090,440 1108,465 1124,480 L1124,0 Z" fill="var(--brand-blue)"/>
    <path d="M0,168 C200,158 420,172 560,205 L640,540 C540,600 470,690 412,787 L0,787 Z" fill="url(#blueFill)"/>
    <path d="M340,168 C440,176 510,188 560,205 L555,220 C500,205 430,192 340,182 Z" fill="var(--brand-green)"/>
    <path d="M640,540 C540,600 470,690 412,787 L442,787 C495,700 560,615 650,560 Z" fill="var(--brand-green)"/>
  </svg>

  <div class="abs brand" style="left:44px;top:48px;font-size:31px">
    <span class="brand__dot" style="width:62px;height:62px"></span>Brookvale Networks
  </div>

  <div class="abs headline-bar" style="left:43px;top:213px;height:142px"></div>
  <h1 class="abs headline" style="left:62px;top:200px;font-size:76px;line-height:80px">Fast and<br>Reliable</h1>
  <p class="abs subtitle" style="left:44px;top:368px;font-size:28px;line-height:35px">Internet service designed<br>and catered to meet<br>your needs</p>
  <div class="abs divider" style="left:44px;top:490px;width:400px"></div>
  <p class="abs about" style="left:44px;top:516px"><strong>Brookvale Networks</strong> offers fast<br>and reliable internet service without<br>the headaches. No long term<br>contracts or special promotions<br>that expire and raise your rate.<br>We offer a simple monthly rate<br>with bills and features that are<br>easy to understand.</p>

  <div class="abs photo" role="img" aria-label="Photo of a family on a sofa using a tablet, phone and laptop" style="left:524px;top:35px;width:570px;height:570px"></div>

  <div class="abs cta" style="left:597px;top:630px;font-size:33px;color:var(--brand-blue)">
    <svg width="30" height="34" viewBox="0 0 30 34" aria-hidden="true"><rect x="2" y="2" width="22" height="28" rx="3" fill="none" stroke="var(--brand-blue)" stroke-width="2.5"/><path d="M7,10h12M7,16h12M7,22h7" stroke="var(--brand-blue)" stroke-width="2.5"/><path d="M18,30l8-10 3,2-8,10-4,1z" fill="var(--brand-blue)"/></svg>
    Sign up today!
  </div>
  <div class="abs phone-line" style="left:600px;top:676px;font-size:36px">
    <svg width="26" height="26" viewBox="0 0 24 24" aria-hidden="true"><path d="M6.6,10.8a15,15 0 0 0 6.6,6.6l2.2-2.2a1,1 0 0 1 1-.25 11,11 0 0 0 3.6.6 1,1 0 0 1 1,1V20a1,1 0 0 1-1,1A17,17 0 0 1 3,4a1,1 0 0 1 1-1h3.5a1,1 0 0 1 1,1 11,11 0 0 0 .6,3.6 1,1 0 0 1-.25,1z" fill="var(--ink)"/></svg>
    844-555-0172
  </div>
  <div class="abs web-line" style="left:602px;top:724px;font-size:24px">
    <svg width="22" height="22" viewBox="0 0 24 24" aria-hidden="true"><circle cx="12" cy="12" r="10" fill="none" stroke="var(--ink)" stroke-width="2"/><path d="M2,12h20M12,2c-4,5-4,15 0,20M12,2c4,5 4,15 0,20" fill="none" stroke="var(--ink)" stroke-width="1.8"/></svg>
    www.brookvale-networks.example
  </div>
</section>

<section class="card card--back">
  <svg class="shapes" viewBox="0 0 1124 787" aria-hidden="true">
    <defs>
      <linearGradient id="blueFillBack" x1="0" y1="0" x2="1" y2="1">
        <stop offset="0" stop-color="#0a4fa0"/>
        <stop offset="1" stop-color="#0a3d8c"/>
      </linearGradient>
    </defs>
    <path d="M0,0 L530,0 C450,90 440,200 480,330 C530,480 610,600 642,787 L0,787 Z" fill="url(#blueFillBack)"/>
    <path d="M550,0 C470,90 460,200 500,330 C550,480 630,600 662,787" fill="none" stroke="var(--brand-green)" stroke-width="9"/>
    <path d="M566,0 C486,90 476,200 516,330 C566,480 646,600 678,787" fill="none" stroke="var(--brand-blue)" stroke-width="4"/>
    <path d="M0,705 L62,705 A30,30 0 0 1 62,765 L0,765 Z" fill="var(--brand-green)"/>
  </svg>

  <div class="abs headline-bar" style="left:43px;top:45px;height:125px"></div>
  <h2 class="abs headline" style="left:62px;top:34px;font-size:68px;line-height:70px">Fast and<br>Reliable</h2>
  <p class="abs subtitle" style="left:44px;top:180px;font-size:26px;line-height:31px">Internet service designed<br>and catered to meet<br>your needs</p>
  <div class="abs divider" style="left:40px;top:295px;width:362px"></div>

  <ul class="abs checklist" style="left:40px;top:323px">
    <li><svg width="22" height="22" viewBox="0 0 22 22" aria-hidden="true"><circle cx="11" cy="11" r="11" fill="var(--brand-green)"/><path d="M6,11l3.5,3.5 6.5-7" fill="none" stroke="var(--brand-blue)" stroke-width="2.6"/></svg>Fast and reliable internet service</li>
    <li><svg width="22" height="22" viewBox="0 0 22 22" aria-hidden="true"><circle cx="11" cy="11" r="11" fill="var(--brand-green)"/><path d="M6,11l3.5,3.5 6.5-7" fill="none" stroke="var(--brand-blue)" stroke-width="2.6"/></svg>Real customer support</li>
    <li><svg width="22" height="22" viewBox="0 0 22 22" aria-hidden="true"><circle cx="11" cy="11" r="11" fill="var(--brand-green)"/><path d="M6,11l3.5,3.5 6.5-7" fill="none" stroke="var(--brand-blue)" stroke-width="2.6"/></svg>Less buffering while streaming</li>
    <li><svg width="22" height="22" viewBox="0 0 22 22" aria-hidden="true"><circle cx="11" cy="11" r="11" fill="var(--brand-green)"/><path d="M6,11l3.5,3.5 6.5-7" fill="none" stroke="var(--brand-blue)" stroke-width="2.6"/></svg>Fast web browsing</li>
    <li><svg width="22" height="22" viewBox="0 0 22 22" aria-hidden="true"><circle cx="11" cy="11" r="11" fill="var(--brand-green)"/><path d="M6,11l3.5,3.5 6.5-7" fill="none" stroke="var(--brand-blue)" stroke-width="2.6"/></svg>Gaming without the lag</li>
    <li><svg width="22" height="22" viewBox="0 0 22 22" aria-hidden="true"><circle cx="11" cy="11" r="11" fill="var(--brand-green)"/><path d="M6,11l3.5,3.5 6.5-7" fill="none" stroke="var(--brand-blue)" stroke-width="2.6"/></svg>Wall to wall WiFi coverage</li>
    <li><svg width="22" height="22" viewBox="0 0 22 22" aria-hidden="true"><circle cx="11" cy="11" r="11" fill="var(--brand-green)"/><path d="M6,11l3.5,3.5 6.5-7" fill="none" stroke="var(--brand-blue)" stroke-width="2.6"/></svg>No introductory charges, one constant rate</li>
    <li><svg width="22" height="22" viewBox="0 0 22 22" aria-hidden="true"><circle cx="11" cy="11" r="11" fill="var(--brand-green)"/><path d="M6,11l3.5,3.5 6.5-7" fill="none" stroke="var(--brand-blue)" stroke-width="2.6"/></svg>Simple and easy to read bills</li>
  </ul>

  <div class="abs cta" style="left:42px;top:709px;font-size:46px;line-height:52px;color:var(--brand-green);gap:22px">
    <svg width="44" height="50" viewBox="0 0 30 34" aria-hidden="true"><rect x="2" y="2" width="22" height="28" rx="3" fill="none" stroke="var(--brand-blue)" stroke-width="2.5"/><path d="M7,10h12M7,16h12M7,22h7" stroke="var(--brand-blue)" stroke-width="2.5"/><path d="M18,30l8-10 3,2-8,10-4,1z" fill="var(--brand-blue)"/></svg>
    Sign up today!
  </div>

  <div class="abs brand" style="left:545px;top:40px;font-size:22px;gap:9px">
    <span class="brand__dot" style="width:44px;height:44px"></span>Brookvale Networks
  </div>
  <div class="abs stamp-box" style="left:951px;top:41px;width:123px;height:134px"></div>
  <div class="abs address-line" style="left:687px;top:311px;width:387px"></div>
  <div class="abs address-line" style="left:687px;top:379px;width:387px"></div>
  <div class="abs address-line" style="left:687px;top:444px;width:387px"></div>
  <div class="abs address-line" style="left:687px;top:509px;width:387px"></div>

  <div class="abs phone-line" style="left:734px;top:684px;font-size:38px">
    <svg width="26" height="26" viewBox="0 0 24 24" aria-hidden="true"><path d="M6.6,10.8a15,15 0 0 0 6.6,6.6l2.2-2.2a1,1 0 0 1 1-.25 11,11 0 0 0 3.6.6 1,1 0 0 1 1,1V20a1,1 0 0 1-1,1A17,17 0 0 1 3,4a1,1 0 0 1 1-1h3.5a1,1 0 0 1 1,1 11,11 0 0 0 .6,3.6 1,1 0 0 1-.25,1z" fill="var(--ink)"/></svg>
    844-555-0172
  </div>
  <div class="abs web-line" style="left:743px;top:735px;font-size:16px;gap:12px">
    <svg width="15" height="15" viewBox="0 0 24 24" aria-hidden="true"><circle cx="12" cy="12" r="10" fill="none" stroke="var(--ink)" stroke-width="2"/><path d="M2,12h20M12,2c-4,5-4,15 0,20M12,2c4,5 4,15 0,20" fill="none" stroke="var(--ink)" stroke-width="1.8"/></svg>
    www.brookvale-networks.example
  </div>
</section>

</body>
</html>
```